Pediatric Speech Therapy Private Practice Announcement

I opened a solo private practice as a pediatric speech therapist in June 2014 in Orinda, CA in June 2014. I have 25 years experience in the field and worked as the Director of a very successful group practice of speech therapists in nearby Walnut Creek. I am trying to get my own name established in the local community and letting people know that I now have my own practice, which I call Halvorsen Speech-Language Center.

I would like this postcard to advertise low-cost speech-language screenings offered to nearby preschools.

Target Market(s)

Preschool Directors

Industry/Entity Type

Call

Requirements
Must have
• Photos of children, preschool ages, 3-5

Bright colors to get attention

```html
<!DOCTYPE html>
<html lang="en">
<head>
<meta charset="utf-8">
<title>Halvorsen Speech-Language Center – Screening Postcard</title>
<link rel="stylesheet" href="https://fonts.googleapis.com/css2?family=Oswald:wght@500;700&family=Exo+2:wght@400;600&family=Arimo:wght@400;700&display=swap">
<style>
  :root {
    --page: #ece9e4;
    --card: #ffffff;
    --plum: #9b2a7f;
    --plum-dark: #6e1a63;
    --plum-light: #c04a97;
    --lime: #b9c43a;
    --lime-dark: #8e9a1c;
    --teal: #a8dde0;
    --ink: #222222;
    --rule: #c9c9c9;
    --photo-a: #f3c9d9;
    --photo-b: #9ccbe8;
    --photo-c: #f4f1ee;
  }
  * { box-sizing: border-box; margin: 0; padding: 0; }
  html, body { width: 1200px; height: 1000px; overflow: hidden; }
  body { background: var(--page); position: relative; font-family: "Arimo", sans-serif; }

  .postcard {
    position: absolute;
    background: var(--card);
    box-shadow: 0 10px 28px rgba(0,0,0,.22);
    overflow: hidden;
  }

  /* Front */
  .postcard--front { left: 50px; top: 40px; width: 640px; height: 450px; }
  .front__band {
    position: absolute; inset: 0 0 auto 0; height: 232px;
    background: linear-gradient(120deg, var(--plum-light) 0%, var(--plum) 45%, var(--plum-dark) 100%);
    clip-path: polygon(0 0, 100% 0, 100% 100%, 0 86%);
    z-index: 2;
  }
  .front__band-edge {
    position: absolute; left: 0; right: 0; top: 190px; height: 50px;
    background: var(--plum-dark);
    clip-path: polygon(0 0, 100% 26%, 100% 100%, 0 56%);
    z-index: 1;
  }
  .front__photo {
    position: absolute; left: 0; right: 0; top: 190px; bottom: 0;
    background:
      radial-gradient(circle at 30% 40%, var(--photo-b) 0 16%, transparent 30%),
      radial-gradient(circle at 60% 70%, var(--photo-a) 0 14%, transparent 30%),
      linear-gradient(160deg, var(--photo-c), #e3dfdb);
  }
  .front__text {
    position: absolute; left: 250px; right: 20px; top: 14px;
    text-align: center; color: #fff; z-index: 3;
  }
  .business-name { font-weight: 600; line-height: 1.1; }
  .front__text .business-name { font-family: "Exo 2", sans-serif; font-size: 28px; }
  .front__lead { font-family: "Exo 2", sans-serif; font-size: 16px; line-height: 1.3; margin-top: 8px; }
  .front__offer { font-family: "Exo 2", sans-serif; font-weight: 600; font-size: 20px; line-height: 1.25; }
  .front__where { font-family: "Exo 2", sans-serif; font-size: 15px; margin-top: 2px; }

  .badge { position: absolute; left: 38px; top: 36px; width: 190px; height: 190px; z-index: 4; }
  .badge svg { width: 100%; height: 100%; filter: drop-shadow(0 3px 4px rgba(0,0,0,.3)); }
  .badge__text {
    position: absolute; left: 0; top: 0; width: 190px; height: 190px;
    display: flex; flex-direction: column; align-items: center; justify-content: center;
    transform: rotate(-32deg);
    font-family: "Oswald", sans-serif; font-weight: 700; color: var(--ink);
    text-align: center; line-height: 1.05;
  }
  .badge__new { font-size: 30px; }
  .badge__line { font-size: 15px; }

  /* Back */
  .postcard--back { left: 570px; top: 530px; width: 580px; height: 420px; }
  .back__message { position: absolute; left: 24px; top: 26px; width: 250px; text-align: center; }
  .back__message .business-name { font-family: "Arimo", sans-serif; font-weight: 700; font-size: 22px; color: var(--plum); }
  .back__stat { font-weight: 700; font-size: 12.5px; line-height: 1.35; margin-top: 20px; color: var(--ink); }
  .back__detail { font-size: 12px; line-height: 1.4; margin-top: 14px; color: var(--ink); }
  .back__cta {
    position: absolute; left: 0; top: 330px; width: 290px; height: 72px;
    background: var(--teal);
    font-family: "Oswald", sans-serif; font-weight: 500; font-size: 13px;
    line-height: 1.3; text-align: center; color: var(--ink);
    display: flex; align-items: center; justify-content: center; padding: 0 18px;
  }
  .back__divider { position: absolute; left: 300px; top: 22px; bottom: 22px; width: 1px; background: var(--rule); }
  .back__stamp { position: absolute; right: 30px; top: 26px; width: 104px; height: 112px; border: 3px solid #d4d4d4; }
  .back__address { position: absolute; left: 320px; right: 30px; top: 196px; }
  .back__address-line { height: 1px; background: var(--rule); margin-bottom: 33px; }
</style>
</head>
<body>

<section class="postcard postcard--front" aria-label="Postcard front">
  <div class="front__photo" role="img" aria-label="Photo of four smiling preschool children lying in a circle on a white floor"></div>
  <div class="front__band-edge"></div>
  <div class="front__band"></div>

  <div class="front__text">
    <div class="business-name">Halvorsen Speech-Language Center</div>
    <p class="front__lead">Owned and operated by<br>Maren Halvorsen, MS, CCC-SLP, will be offering</p>
    <p class="front__offer">low cost ($40) on site<br>speech-language screenings</p>
    <p class="front__where">at preschools this Fall in the Lamorinda area.</p>
  </div>

  <div class="badge">
    <svg viewBox="0 0 150 150" aria-hidden="true">
      <polygon fill="var(--lime)" stroke="var(--lime-dark)" stroke-width="1.5" points="145,75 132.3,84 141.6,96.6 126.7,101.3 131.6,116.2 116,116 116.2,131.6 101.3,126.7 96.6,141.6 84,132.3 75,145 66,132.3 53.4,141.6 48.7,126.7 33.8,131.6 34,116 18.4,116.2 23.3,101.3 8.4,96.6 17.7,84 5,75 17.7,66 8.4,53.4 23.3,48.7 18.4,33.8 34,34 33.8,18.4 48.7,23.3 53.4,8.4 66,17.7 75,5 84,17.7 96.6,8.4 101.3,23.3 116.2,18.4 116,34 131.6,33.8 126.7,48.7 141.6,53.4 132.3,66"/>
    </svg>
    <div class="badge__text">
      <span class="badge__new">NEW</span>
      <span class="badge__line">PEDIATRIC</span>
      <span class="badge__line">SPEECH THERAPY</span>
      <span class="badge__line">PRACTICE IN</span>
      <span class="badge__line">ORINDA</span>
    </div>
  </div>
</section>

<section class="postcard postcard--back" aria-label="Postcard back">
  <div class="back__message">
    <div class="business-name">Halvorsen Speech-Language Center</div>
    <p class="back__stat">Speech-language disorders affect 1 in 10 children. Early identification is the first step to early intervention.</p>
    <p class="back__detail">Speech-language screenings reliably identify preschoolers at risk for speech/articulation impairments, fluency/stuttering disorders, or problems with language comprehension or language expression.</p>
  </div>
  <div class="back__cta">CALL (925) 555-0148 FOR ADDITIONAL INFORMATION, OR TO SCHEDULE AN ON-SITE SCREENING AT YOUR PRESCHOOL TODAY!</div>
  <div class="back__divider"></div>
  <div class="back__stamp"></div>
  <div class="back__address">
    <div class="back__address-line"></div>
    <div class="back__address-line"></div>
    <div class="back__address-line"></div>
    <div class="back__address-line"></div>
    <div class="back__address-line"></div>
  </div>
</section>

</body>
</html>
```